New Coffee Packaging

Update/refresh/modernize range of 1 kg Coffee packaging

Industry/Entity Type

Hospitalty

Requirements
Must have
• Clean. crisp, eye catching
Nice to have
• Verdano means 'Height' specialty coffee is grown at high altitudes, peaks. mountains

```html
<!DOCTYPE html>
<html lang="en">
<head>
<meta charset="utf-8">
<title>Verdano Coffee – 1 kg Range</title>
<link href="https://fonts.googleapis.com/css2?family=Saira+Condensed:wght@600&family=Fira+Sans:wght@400;500;600&display=swap" rel="stylesheet">
<style>
  :root {
    --backdrop: #e6e6e6;
    --paper: #f7f7f5;
    --ink: #3b3b3b;
    --ink-soft: #555;
    --rule: #b48a3c;
    --red: #c8273a;
    --gold: #b8862e;
    --black: #2f2f2f;
    --red-art: #e7a9b0;
    --gold-art: #e3cfa6;
    --black-art: #c9c9c9;
  }
  * { box-sizing: border-box; margin: 0; padding: 0; }
  html, body { width: 1200px; height: 900px; overflow: hidden; }
  body {
    background: var(--backdrop);
    font-family: "Fira Sans", sans-serif;
    color: var(--ink);
  }
  .range {
    position: relative;
    width: 1200px; height: 900px;
    display: flex; justify-content: center; align-items: center; gap: 42px;
  }
  .bag {
    --accent: var(--red);
    position: relative;
    width: 330px; height: 700px;
    background: var(--paper);
    border-left: 10px solid var(--accent);
    border-right: 10px solid var(--accent);
    border-radius: 6px 6px 3px 3px;
    box-shadow: 0 10px 24px rgba(0,0,0,.12);
    display: flex; flex-direction: column; align-items: center;
    padding-top: 58px;
    overflow: hidden;
  }
  .bag::before {
    content: ""; position: absolute; top: 0; left: 0; right: 0; height: 34px;
    background: var(--paper); border-bottom: 1px solid #e2e2e0;
  }
  .bag--summit { --accent: var(--red); --art: var(--red-art); }
  .bag--highland { --accent: var(--gold); --art: var(--gold-art); }
  .bag--classic { --accent: var(--black); --art: var(--black-art); }

  .brand-name {
    font-family: "Saira Condensed", sans-serif;
    font-weight: 600; font-size: 70px; line-height: 1;
    color: var(--ink); letter-spacing: -1px;
  }
  .blend-tag {
    margin-top: 30px;
    background: var(--accent); color: #fff;
    font-weight: 600; font-size: 17px; letter-spacing: 3px;
    padding: 6px 22px; border-radius: 4px;
  }
  .illustration {
    margin-top: 22px;
    width: 250px; height: 200px; border-radius: 10px;
    background: radial-gradient(ellipse at 50% 55%, var(--art) 0%, rgba(255,255,255,0) 72%);
  }
  .bag--classic .illustration { margin-top: 48px; height: 270px; width: 210px; }

  .cup-profile { width: 230px; margin-top: 22px; }
  .cup-profile h3 { font-size: 13px; font-weight: 600; padding-bottom: 7px; border-bottom: 1px solid var(--rule); }
  .cup-profile ul { list-style: none; padding: 9px 0 8px; border-bottom: 1px solid var(--rule); }
  .cup-profile li { font-size: 13.5px; line-height: 1.45; color: var(--ink-soft); }

  .brew-methods {
    position: absolute; left: 22px; bottom: 78px;
    display: flex; gap: 12px;
  }
  .bag--classic .brew-methods { bottom: 126px; }
  .brew { display: flex; flex-direction: column; align-items: center; gap: 2px; width: 40px; }
  .brew svg { width: 22px; height: 22px; }
  .brew span { font-size: 9px; color: var(--ink-soft); }
  .brew i { width: 11px; height: 11px; border: 1px solid #777; border-radius: 50%; margin-top: 2px; }

  .est-seal {
    position: absolute; right: 14px; bottom: 64px;
    width: 62px; height: 62px; border-radius: 50%;
    background: #3a3a3a; border: 3px solid #fff; box-shadow: 0 0 0 1px #3a3a3a;
  }
  .bag--classic .est-seal { bottom: 112px; }

  .weight-band {
    position: absolute; left: 0; right: 0; bottom: 0; height: 52px;
    background: var(--accent); color: #fff;
    display: flex; align-items: center; justify-content: center;
    font-weight: 600; font-size: 17px;
  }
  .bag--classic .weight-band { height: 100px; align-items: flex-start; padding-top: 14px; }
</style>
</head>
<body>
<main class="range">

  <article class="bag bag--summit">
    <h2 class="brand-name">Verdano</h2>
    <div class="blend-tag">SUMMIT</div>
    <div class="illustration" role="img" aria-label="Red line drawing of mountains, coffee cherries and a cup of coffee"></div>
    <section class="cup-profile">
      <h3>CUP PROFILE:</h3>
      <ul><li>Dark chocolate</li><li>Caramel</li><li>Malt</li><li>Lower acidity and full body</li></ul>
    </section>
    <div class="brew-methods">
      <div class="brew"><svg viewBox="0 0 24 24" fill="none" stroke="#444" stroke-width="1.4"><path d="M3 6h18l-7 10h-4z"/><path d="M8 20h8"/></svg><span>Filter</span><i></i></div>
      <div class="brew"><svg viewBox="0 0 24 24" fill="none" stroke="#444" stroke-width="1.4"><circle cx="8" cy="9" r="4"/><path d="M11 11l10 7"/></svg><span>Espresso</span><i></i></div>
      <div class="brew"><svg viewBox="0 0 24 24" fill="none" stroke="#444" stroke-width="1.4"><rect x="7" y="7" width="10" height="14" rx="1"/><path d="M12 2v5M9 3h6M17 10h3v7h-3"/></svg><span>Plunger</span><i></i></div>
      <div class="brew"><svg viewBox="0 0 24 24" fill="#444"><ellipse cx="9" cy="8" rx="4" ry="5"/><ellipse cx="15" cy="16" rx="4" ry="5"/></svg><span>Beans</span><i></i></div>
    </div>
    <div class="est-seal" aria-hidden="true"></div>
    <div class="weight-band">1 kg</div>
  </article>

  <article class="bag bag--highland">
    <h2 class="brand-name">Verdano</h2>
    <div class="blend-tag">HIGHLAND</div>
    <div class="illustration" role="img" aria-label="Gold line drawing of a coffee grower picking cherries from a branch"></div>
    <section class="cup-profile">
      <h3>CUP PROFILE:</h3>
      <ul><li>Honey</li><li>Stonefruit</li><li>Toffee</li><li>Medium/high sweetness</li></ul>
    </section>
    <div class="brew-methods">
      <div class="brew"><svg viewBox="0 0 24 24" fill="none" stroke="#444" stroke-width="1.4"><path d="M3 6h18l-7 10h-4z"/><path d="M8 20h8"/></svg><span>Filter</span><i></i></div>
      <div class="brew"><svg viewBox="0 0 24 24" fill="none" stroke="#444" stroke-width="1.4"><circle cx="8" cy="9" r="4"/><path d="M11 11l10 7"/></svg><span>Espresso</span><i></i></div>
      <div class="brew"><svg viewBox="0 0 24 24" fill="none" stroke="#444" stroke-width="1.4"><rect x="7" y="7" width="10" height="14" rx="1"/><path d="M12 2v5M9 3h6M17 10h3v7h-3"/></svg><span>Plunger</span><i></i></div>
      <div class="brew"><svg viewBox="0 0 24 24" fill="#444"><ellipse cx="9" cy="8" rx="4" ry="5"/><ellipse cx="15" cy="16" rx="4" ry="5"/></svg><span>Beans</span><i></i></div>
    </div>
    <div class="est-seal" aria-hidden="true"></div>
    <div class="weight-band">1 kg</div>
  </article>

  <article class="bag bag--classic">
    <h2 class="brand-name">Verdano</h2>
    <div class="illustration" role="img" aria-label="Black ink drawing of a hand-crank coffee grinder with beans"></div>
    <div class="brew-methods">
      <div class="brew"><svg viewBox="0 0 24 24" fill="none" stroke="#444" stroke-width="1.4"><path d="M3 6h18l-7 10h-4z"/><path d="M8 20h8"/></svg><span>Filter</span><i></i></div>
      <div class="brew"><svg viewBox="0 0 24 24" fill="none" stroke="#444" stroke-width="1.4"><circle cx="8" cy="9" r="4"/><path d="M11 11l10 7"/></svg><span>Espresso</span><i></i></div>
      <div class="brew"><svg viewBox="0 0 24 24" fill="none" stroke="#444" stroke-width="1.4"><rect x="7" y="7" width="10" height="14" rx="1"/><path d="M12 2v5M9 3h6M17 10h3v7h-3"/></svg><span>Plunger</span><i></i></div>
      <div class="brew"><svg viewBox="0 0 24 24" fill="#444"><ellipse cx="9" cy="8" rx="4" ry="5"/><ellipse cx="15" cy="16" rx="4" ry="5"/></svg><span>Beans</span><i></i></div>
    </div>
    <div class="est-seal" aria-hidden="true"></div>
    <div class="weight-band">1 kg</div>
  </article>

</main>
</body>
</html>
```